Christmas Flyer

Hi,
We are needing a flyer that communicates a Christmas message for our cafe.
We'd like to advertise:
"To all of our loyal customers, if you are lucky enough to be working Christmas Day, we will be open and serving you FREE COFFEE from 6am - 10am.
Thank you for all your support over the last 12 months, we hope you have a very Merry Christmas, and have a happy and safe holidays from Harbour Lantern Kitchen"

I have included our logo, and one of our previous flyers.

You can also check out our instagram. Instagram @harbourlanternkitchen

Industry/Entity Type

Cafe

```html
<!DOCTYPE html>
<html lang="en">
<head>
<meta charset="utf-8">
<title>Christmas Free Coffee Flyer – Harbour Lantern Kitchen</title>
<link rel="stylesheet" href="https://fonts.googleapis.com/css2?family=Cormorant+Garamond:ital,wght@1,600&family=Pinyon+Script&display=swap">
<style>
  :root {
    --bg-light: #e6f0ae;
    --bg-mid: #c3da66;
    --bg-deep: #99bd3a;
    --pine-dark: #1d5a1b;
    --pine-mid: #3a8a28;
    --pine-soft: rgba(58,138,40,0);
    --berry-red: #d4141c;
    --coffee-brown: #6a3a1c;
    --cup-cream: #f4efe6;
  }
  * { margin: 0; padding: 0; box-sizing: border-box; }
  html, body { width: 849px; height: 1200px; overflow: hidden; background: #fff; }
  .flyer {
    position: relative;
    width: 849px;
    height: 1200px;
    overflow: hidden;
    background:
      radial-gradient(circle at 30% 30%, rgba(255,255,255,.3) 0 40px, transparent 42px),
      radial-gradient(circle at 72% 42%, rgba(255,255,255,.25) 0 55px, transparent 57px),
      radial-gradient(circle at 40% 72%, rgba(255,255,255,.22) 0 35px, transparent 37px),
      radial-gradient(circle at 62% 20%, rgba(255,255,255,.2) 0 28px, transparent 30px),
      radial-gradient(ellipse at 50% 50%, var(--bg-light) 0%, var(--bg-mid) 60%, var(--bg-deep) 100%);
    font-family: "Cormorant Garamond", Georgia, serif;
    font-style: italic;
    font-weight: 600;
    color: var(--berry-red);
  }

  /* Garland frame: one area, banded around the edges */
  .garland { position: absolute; inset: 0; }
  .garland__band { position: absolute; }
  .garland__band--top {
    top: 0; left: 0; right: 0; height: 95px;
    background: linear-gradient(to bottom, var(--pine-dark), var(--pine-mid) 55%, var(--pine-soft));
  }
  .garland__band--bottom {
    bottom: 0; left: 0; right: 0; height: 105px;
    background: linear-gradient(to top, var(--pine-dark), var(--pine-mid) 55%, var(--pine-soft));
  }
  .garland__band--left {
    top: 0; bottom: 0; left: 0; width: 125px;
    background: linear-gradient(to right, var(--pine-dark), var(--pine-mid) 55%, var(--pine-soft));
  }
  .garland__band--right {
    top: 0; bottom: 0; right: 0; width: 125px;
    background: linear-gradient(to left, var(--pine-dark), var(--pine-mid) 55%, var(--pine-soft));
  }

  .message {
    position: absolute;
    left: 0;
    width: 100%;
    text-align: center;
    font-size: 28px;
    line-height: 44px;
  }
  .message--intro { top: 136px; }
  .message--thanks { top: 660px; }

  .headline {
    position: absolute;
    top: 440px;
    left: 20px;
    width: 100%;
    text-align: center;
    font-family: "Pinyon Script", cursive;
    font-style: normal;
    font-weight: 400;
    font-size: 110px;
    line-height: 140px;
    color: var(--coffee-brown);
  }
  .coffee-cup {
    position: absolute;
    left: 125px;
    top: 558px;
    width: 145px;
    height: 105px;
    border-radius: 40%;
    background: radial-gradient(ellipse at 50% 50%, var(--cup-cream) 0 55%, rgba(244,239,230,.4) 75%, rgba(244,239,230,0) 100%);
  }
  .hours {
    position: absolute;
    top: 578px;
    left: 325px;
    font-size: 31px;
    line-height: 44px;
  }
  .sign-off {
    position: absolute;
    left: 540px;
    width: 300px;
    top: 928px;
    text-align: center;
    font-size: 27px;
    line-height: 42px;
  }
  .sign-off__from { display: block; padding-left: 110px; }

  .brand-mark {
    position: absolute;
    left: 0;
    width: 100%;
    top: 1056px;
    display: flex;
    justify-content: center;
    align-items: center;
    gap: 8px;
    font-size: 22px;
  }
  .brand-mark__dot {
    width: 14px;
    height: 14px;
    border-radius: 50%;
    background: var(--berry-red);
  }
</style>
</head>
<body>
<main class="flyer">
  <div class="garland" role="img" aria-label="Frame of green pine branches with red holly berries around the edges">
    <div class="garland__band garland__band--top"></div>
    <div class="garland__band garland__band--bottom"></div>
    <div class="garland__band garland__band--left"></div>
    <div class="garland__band garland__band--right"></div>
  </div>

  <p class="message message--intro">
    To all of our loyal customers,<br>
    if you are lucky enough<br>
    to be working Christmas Day,<br>
    we will be open and serving you
  </p>

  <h1 class="headline">Free Coffee</h1>

  <div class="coffee-cup" role="img" aria-label="Cup of coffee on a white saucer with a spoon"></div>

  <p class="hours">from 6am - 10am.</p>

  <p class="message message--thanks">
    Thank you for all your support<br>
    over the last 12 months,<br>
    we hope you have<br>
    a very Merry Christmas,<br>
    and have a happy and safe holidays.
  </p>

  <p class="sign-off">
    <span class="sign-off__from">from</span>
    Harbour Lantern Kitchen
  </p>

  <div class="brand-mark">
    <span class="brand-mark__dot"></span>
    <span class="brand-mark__name">Harbour Lantern Kitchen</span>
  </div>
</main>
</body>
</html>
```